New Facebook Banner

Hi
We are operating Ramen shop in Australia.(http://mizunokobowls.com)
I want to create new design for our Facebook banner and title is "Free Ramen on your Birthday".
Sample attached is our existing banner design. We would like to make it more modern and sophisticated.
We are so looking forward to seeing your design for our free ramen promotion.

https://www.facebook.com/mizunokobowls/

Industry/Entity Type

Japanese Restaurant

Font styles to use
Sans Serif

```html
<!DOCTYPE html>
<html lang="en">
<head>
<meta charset="utf-8">
<title>Free Ramen on Your Birthday – Facebook Banner</title>
<link rel="stylesheet" href="https://fonts.googleapis.com/css2?family=Open+Sans:wght@600;700;800&display=swap">
<style>
  :root {
    --page-bg: #f6e7a6;
    --orange-deep: #f7950a;
    --orange-mid: #ffaa14;
    --side-orange: #ffa010;
    --yellow-glow: #ffe34a;
    --yellow-light: #fff59a;
    --title-red: #8e0c0c;
    --ribbon-red: #e3150f;
    --ribbon-dark: #b20a08;
    --white: #ffffff;
    --balloon-pink: #d4206a;
    --balloon-gold: #ffc21a;
    --bunting-pink: #e0407a;
    --bunting-yellow: #ffe066;
  }
  html, body {
    margin: 0;
    padding: 0;
    width: 1200px;
    height: 1200px;
    overflow: hidden;
    background: var(--page-bg);
  }
  .canvas {
    width: 1200px;
    height: 1200px;
    display: flex;
    align-items: center;
    justify-content: center;
  }
  .banner {
    display: block;
    width: 1120px;
    height: 425px;
    box-shadow: 0 10px 30px rgba(150, 90, 0, 0.25);
  }
  .headline {
    font-family: "Open Sans", sans-serif;
    font-weight: 800;
  }
  .ribbon-text {
    font-family: "Open Sans", sans-serif;
    font-weight: 700;
    fill: var(--white);
  }
</style>
</head>
<body>
<main class="canvas">
  <svg class="banner" viewBox="0 0 828 314" xmlns="http://www.w3.org/2000/svg" role="img" aria-label="Free Ramen on your birthday">
    <defs>
      <linearGradient id="bg-orange" x1="0" y1="0" x2="0" y2="1">
        <stop offset="0" stop-color="var(--orange-mid)"/>
        <stop offset="1" stop-color="var(--orange-deep)"/>
      </linearGradient>
      <radialGradient id="center-glow" cx="0.5" cy="0.42" r="0.6">
        <stop offset="0" stop-color="#fffbd0"/>
        <stop offset="0.35" stop-color="var(--yellow-light)"/>
        <stop offset="0.75" stop-color="var(--yellow-glow)"/>
        <stop offset="1" stop-color="#ffc21c"/>
      </radialGradient>
      <linearGradient id="free-fill" x1="0" y1="0" x2="0" y2="1">
        <stop offset="0" stop-color="#ffd21f"/>
        <stop offset="1" stop-color="#ff9c00"/>
      </linearGradient>
      <linearGradient id="ramen-fill" x1="0" y1="0" x2="0" y2="1">
        <stop offset="0" stop-color="#ffffff"/>
        <stop offset="1" stop-color="#d2d2d2"/>
      </linearGradient>
      <linearGradient id="ribbon-fill" x1="0" y1="0" x2="1" y2="0">
        <stop offset="0" stop-color="var(--ribbon-dark)"/>
        <stop offset="0.5" stop-color="var(--ribbon-red)"/>
        <stop offset="1" stop-color="var(--ribbon-dark)"/>
      </linearGradient>
      <linearGradient id="balloons-tone" x1="0" y1="0" x2="0" y2="1">
        <stop offset="0" stop-color="var(--balloon-pink)" stop-opacity="0"/>
        <stop offset="0.35" stop-color="var(--balloon-pink)" stop-opacity="0.85"/>
        <stop offset="0.7" stop-color="#e8304f"/>
        <stop offset="1" stop-color="var(--balloon-gold)"/>
      </linearGradient>
      <linearGradient id="bunting-tone" x1="0" y1="0" x2="0" y2="1">
        <stop offset="0" stop-color="var(--bunting-pink)" stop-opacity="0.55"/>
        <stop offset="0.5" stop-color="var(--bunting-yellow)" stop-opacity="0.5"/>
        <stop offset="1" stop-color="var(--bunting-yellow)" stop-opacity="0"/>
      </linearGradient>
      <linearGradient id="fade-left" x1="0" y1="0" x2="1" y2="0">
        <stop offset="0" stop-color="#fff"/>
        <stop offset="0.6" stop-color="#fff"/>
        <stop offset="1" stop-color="#000"/>
      </linearGradient>
      <linearGradient id="fade-right" x1="0" y1="0" x2="1" y2="0">
        <stop offset="0" stop-color="#000"/>
        <stop offset="0.4" stop-color="#fff"/>
        <stop offset="1" stop-color="#fff"/>
      </linearGradient>
      <mask id="mask-left" maskContentUnits="objectBoundingBox">
        <rect width="1" height="1" fill="url(#fade-left)"/>
      </mask>
      <mask id="mask-right" maskContentUnits="objectBoundingBox">
        <rect width="1" height="1" fill="url(#fade-right)"/>
      </mask>
    </defs>

    <!-- background -->
    <rect class="banner-bg" width="828" height="314" fill="url(#bg-orange)"/>
    <rect class="side-panel side-panel--left" x="0" y="0" width="140" height="314" fill="var(--side-orange)"/>
    <rect class="side-panel side-panel--right" x="690" y="0" width="138" height="314" fill="var(--side-orange)"/>
    <ellipse class="center-glow" cx="415" cy="150" rx="300" ry="190" fill="url(#center-glow)" transform="rotate(-12 415 150)"/>
    <path class="swoosh" d="M150 314 Q420 250 740 60 L750 80 Q440 290 190 314 Z" fill="#ffb01a" opacity="0.6"/>

    <!-- bunting areas -->
    <rect class="bunting bunting--left" role="img" aria-label="Party bunting flags" x="0" y="0" width="260" height="95" fill="url(#bunting-tone)" mask="url(#mask-left)"/>
    <rect class="bunting bunting--right" role="img" aria-label="Party bunting flags" x="568" y="0" width="260" height="95" fill="url(#bunting-tone)" mask="url(#mask-right)"/>

    <!-- balloon areas -->
    <rect class="balloons balloons--left" role="img" aria-label="Cluster of pink and gold party balloons" x="0" y="150" width="240" height="164" fill="url(#balloons-tone)" mask="url(#mask-left)"/>
    <rect class="balloons balloons--right" role="img" aria-label="Cluster of pink and gold party balloons" x="588" y="150" width="240" height="164" fill="url(#balloons-tone)" mask="url(#mask-right)"/>

    <!-- headline: FREE -->
    <g class="headline headline--free" transform="rotate(-5 350 95)">
      <text x="268" y="122" font-size="84" textLength="168" lengthAdjust="spacingAndGlyphs" fill="var(--title-red)" stroke="var(--title-red)" stroke-width="8" stroke-linejoin="round" transform="translate(0 5)">FREE</text>
      <text x="268" y="122" font-size="84" textLength="168" lengthAdjust="spacingAndGlyphs" fill="url(#free-fill)" stroke="var(--title-red)" stroke-width="6" stroke-linejoin="round" paint-order="stroke">FREE</text>
    </g>

    <!-- headline: RAMEN! -->
    <g class="headline headline--ramen" transform="rotate(-6 418 180)">
      <text x="238" y="220" font-size="108" textLength="362" lengthAdjust="spacingAndGlyphs" fill="var(--title-red)" stroke="var(--title-red)" stroke-width="10" stroke-linejoin="round" transform="translate(0 6)">RAMEN!</text>
      <text x="238" y="220" font-size="108" textLength="362" lengthAdjust="spacingAndGlyphs" fill="url(#ramen-fill)" stroke="var(--title-red)" stroke-width="7" stroke-linejoin="round" paint-order="stroke">RAMEN!</text>
    </g>

    <!-- ribbon -->
    <g class="ribbon" transform="rotate(-8 422 254)">
      <polygon points="266,236 578,236 568,254 578,272 266,272 276,254" fill="url(#ribbon-fill)"/>
      <text class="ribbon-text" x="422" y="261.5" font-size="20" text-anchor="middle" textLength="236" lengthAdjust="spacingAndGlyphs">ON YOUR BIRTHDAY</text>
    </g>
  </svg>
</main>
</body>
</html>
```